Präsentationsvorlagen für die Cloud-Plattform LumaDesk
Zielgruppe
Ich bin ein unabhängiger Berater für die Cloud-Plattform LumaDesk. Zielgruppe sind Unternehmen jeglicher Größe. Das Design sollte schlicht und aufgeräumt sein.
Aufgabenstellung
Dunkler Hintergrund und die Farben aus dem Logo sollten enthalten sein.

```html
<!DOCTYPE html>
<html lang="en">
<head>
<meta charset="utf-8">
<title>LumaDesk presentation templates</title>
<link href="https://fonts.googleapis.com/css2?family=Poppins:wght@400;500;600;700;800&display=swap" rel="stylesheet">
<style>
  :root{
    --orange:#EE7D33;
    --blue:#1B75B3;
    --black:#000000;
    --ink:#1A1A1A;
    --grey:#555555;
    --light:#D9D9D9;
    --white:#FFFFFF;
    --body:#CFCFCF;
  }
  html,body{margin:0;padding:0;width:1200px;height:2400px;overflow:hidden;background:var(--white);}
  .board{display:block;width:1200px;height:2400px;font-family:"Poppins",sans-serif;}
  .slide-bg{fill:var(--black);}
  .brand{font-family:"Poppins",sans-serif;font-weight:600;font-size:13px;fill:var(--orange);}
  .brand-dot{fill:var(--orange);}
  .title{font-family:"Poppins",sans-serif;font-weight:700;fill:var(--white);}
  .kicker{font-family:"Poppins",sans-serif;font-weight:600;font-size:6.5px;fill:var(--orange);}
  .p{font-family:"Poppins",sans-serif;font-weight:400;font-size:5.6px;fill:var(--body);}
  .pc{font-family:"Poppins",sans-serif;font-weight:400;font-size:5.6px;fill:var(--body);text-anchor:middle;}
  .h{font-family:"Poppins",sans-serif;font-weight:700;font-size:10px;fill:var(--white);}
  .hc{font-family:"Poppins",sans-serif;font-weight:700;font-size:10px;fill:var(--white);text-anchor:middle;}
  .ho{font-family:"Poppins",sans-serif;font-weight:700;font-size:11.5px;fill:var(--orange);}
  .pct{font-family:"Poppins",sans-serif;font-weight:700;font-size:13px;fill:var(--white);text-anchor:middle;}
  .num{font-family:"Poppins",sans-serif;font-weight:600;font-size:13px;fill:var(--white);text-anchor:middle;}
  .line-o{stroke:var(--orange);stroke-width:1;fill:none;}
  .line-w{stroke:var(--white);stroke-width:1;fill:none;}
  .photo-warm{fill:url(#warm);}
  .photo-desk{fill:url(#desk);}
  .photo-wood{fill:url(#wood);}
</style>
</head>
<body>
<svg class="board" viewBox="0 0 1200 2400" xmlns="http://www.w3.org/2000/svg">
  <defs>
    <clipPath id="slide-clip"><rect width="610" height="342"/></clipPath>
    <linearGradient id="warm" x1="0" y1="0" x2="1" y2="1">
      <stop offset="0" stop-color="#F6C37A"/><stop offset=".5" stop-color="#B5672C"/><stop offset="1" stop-color="#3A2416"/>
    </linearGradient>
    <linearGradient id="road" x1="0" y1="0" x2="1" y2="0">
      <stop offset="0" stop-color="#5A3A2E"/><stop offset=".6" stop-color="#F2C48A"/><stop offset="1" stop-color="#6E4A36"/>
    </linearGradient>
    <linearGradient id="desk" x1="0" y1="0" x2="1" y2="1">
      <stop offset="0" stop-color="#8A8FA8"/><stop offset=".6" stop-color="#D9B27A"/><stop offset="1" stop-color="#F1EEEA"/>
    </linearGradient>
    <linearGradient id="wood" x1="0" y1="0" x2="1" y2="1">
      <stop offset="0" stop-color="#E8DDCE"/><stop offset=".5" stop-color="#C9A880"/><stop offset="1" stop-color="#EDE6DC"/>
    </linearGradient>
    <symbol id="cloud" viewBox="0 0 100 60">
      <path d="M18 58 C6 58 0 50 0 42 C0 32 8 26 17 26 C18 13 29 4 42 4 C53 4 61 11 64 20 C67 18 71 17 75 17 C88 17 98 27 98 40 C98 50 90 58 80 58 Z"/>
    </symbol>
    <symbol id="down-arrow" viewBox="0 0 10 22">
      <rect x="3" y="0" width="4" height="2"/><rect x="3" y="4" width="4" height="2"/><rect x="3" y="8" width="4" height="5"/>
      <path d="M0 13 H10 L5 22 Z"/>
    </symbol>
    <g id="logo">
      <circle class="brand-dot" cx="-8" cy="-4" r="4"/>
      <text class="brand" x="0" y="0">brightpath</text>
    </g>
  </defs>

  <!-- Row 1 left: cover -->
  <g transform="translate(22 56) scale(0.931)" clip-path="url(#slide-clip)">
    <rect class="slide-bg" width="610" height="342"/>
    <circle class="photo-warm" cx="500" cy="145" r="145" role="img" aria-label="Photo of a business handshake"/>
    <path class="line-o" d="M345 40 A150 150 0 0 0 420 285"/>
    <path class="line-o" d="M330 75 A170 170 0 0 0 465 310"/>
    <path class="line-o" d="M362 30 A130 130 0 0 0 360 205"/>
    <circle cx="420" cy="285" r="2.5" fill="var(--orange)"/>
    <circle cx="465" cy="310" r="2.5" fill="var(--orange)"/>
    <circle cx="345" cy="40" r="2.5" fill="var(--orange)"/>
    <circle cx="168" cy="100" r="12" fill="var(--orange)"/>
    <text class="brand" x="100" y="132" style="font-size:26px">brightpath</text>
    <text class="title" x="26" y="197" style="font-size:38px;font-weight:800">HELPING YOU</text>
    <text x="27" y="220" style="font-size:11.5px;fill:var(--white);letter-spacing:1.6px;font-family:'Poppins',sans-serif">solve complex business requirements</text>
  </g>

  <!-- Row 1 right: vision -->
  <g transform="translate(610 56) scale(0.931)" clip-path="url(#slide-clip)">
    <rect class="slide-bg" width="610" height="342"/>
    <path d="M0 76 H188 A94 94 0 0 1 188 264 H0 Z" fill="url(#road)" role="img" aria-label="Photo of a sunlit road marked with the word vision"/>
    <path class="line-o" d="M0 66 H46"/><circle cx="46" cy="66" r="2.5" fill="var(--orange)"/>
    <path class="line-o" d="M0 285 H92"/><circle cx="92" cy="285" r="2.5" fill="var(--orange)"/>
    <use href="#logo" x="520" y="56"/>
    <text class="kicker" x="328" y="98">INTRODUCTION</text>
    <text class="title" x="328" y="125" style="font-size:23px">We Utilize</text>
    <text class="title" x="328" y="152" style="font-size:23px">Your Vision</text>
    <text class="p"><tspan x="328" y="172">Lorem ipsum dolor sit amet, consectetur adipiscing elit. Duis</tspan><tspan x="328" dy="7.5">suscipit, arcu sed sodales dignissim, nisi ipsum ultrices risus,</tspan><tspan x="328" dy="7.5">facilisis ultrices augue urna ac tortor. Donec convallis sem ac</tspan><tspan x="328" dy="7.5">nisi posuere, ut varius erat tincidunt. Integer quis tempor nunc.</tspan><tspan x="328" dy="7.5">Ut elementum nec massa sed hendrerit. Vivamus lorem risus,</tspan><tspan x="328" dy="7.5">tempor ut molestie a, rhoncus vitae massa onec sed viverra.</tspan></text>
  </g>

  <!-- Row 2 left: overview -->
  <g transform="translate(22 384) scale(0.931)" clip-path="url(#slide-clip)">
    <rect class="slide-bg" width="610" height="342"/>
    <path class="line-o" d="M0 16 H122"/><path class="line-o" d="M0 26 H93"/><circle cx="122" cy="16" r="2.5" fill="var(--orange)"/>
    <circle class="photo-desk" cx="126" cy="180" r="98" role="img" aria-label="Photo of a person writing at a desk"/>
    <use href="#cloud" x="45" y="246" width="80" height="44" fill="var(--orange)"/>
    <use href="#logo" x="520" y="56"/>
    <text class="kicker" x="264" y="84">AGENDA</text>
    <text class="title" x="264" y="110" style="font-size:23px">Overview</text>
    <text class="p"><tspan x="264" y="130">Lorem ipsum dolor sit amet, consectetur adipiscing elit. Duis suscipit, arcu sed sodales</tspan><tspan x="264" dy="7.5">dignissim, nisi ipsum ultrices risus, facilisis ultrices augue urna ac tortor. Donec convallis</tspan><tspan x="264" dy="7.5">sem ac nisi posuere, ut varius erat tincidunt. Integer quis tempor nunc ut elementum.</tspan></text>
    <path class="line-o" d="M266 210 H284"/><circle cx="284" cy="210" r="2.5" fill="var(--orange)"/>
    <text class="ho"><tspan x="266" y="230">Our Vision</tspan><tspan x="266" dy="13">and Mission</tspan></text>
    <text class="p"><tspan x="266" y="256">Lorem ipsum dolor sit amet, consectetur</tspan><tspan x="266" dy="7.5">adipiscing elit. Duis suscipit, arcu sed</tspan><tspan x="266" dy="7.5">sodales dignissim, nisi ipsum ultrices</tspan><tspan x="266" dy="7.5">risus facilisis.</tspan></text>
    <path class="line-o" d="M433 210 H451"/><circle cx="451" cy="210" r="2.5" fill="var(--orange)"/>
    <text class="ho"><tspan x="433" y="230">Empowering Cloud</tspan><tspan x="433" dy="13">Computing Solutions</tspan></text>
    <text class="p"><tspan x="433" y="256">Lorem ipsum dolor sit amet, consectetur</tspan><tspan x="433" dy="7.5">adipiscing elit. Duis suscipit, arcu sed</tspan><tspan x="433" dy="7.5">sodales dignissim, nisi ipsum ultrices</tspan><tspan x="433" dy="7.5">risus facilisis.</tspan></text>
  </g>

  <!-- Row 2 right: about -->
  <g transform="translate(610 384) scale(0.931)" clip-path="url(#slide-clip)">
    <rect class="slide-bg" width="610" height="342"/>
    <use href="#cloud" x="20" y="150" width="120" height="100" fill="var(--blue)"/>
    <use href="#cloud" x="230" y="90" width="120" height="90" fill="var(--blue)"/>
    <circle cx="160" cy="140" r="90" fill="var(--orange)"/>
    <circle cx="240" cy="230" r="55" fill="var(--orange)"/>
    <circle class="photo-wood" cx="180" cy="178" r="100" role="img" aria-label="Photo of hands arranging wooden blocks showing a light bulb"/>
    <path class="line-o" d="M230 85 H312"/><circle cx="312" cy="85" r="2.5" fill="var(--orange)"/>
    <path class="line-o" d="M96 268 H172"/><circle cx="96" cy="268" r="2.5" fill="var(--orange)"/>
    <use href="#logo" x="520" y="56"/>
    <text class="kicker" x="376" y="80">ABOUT</text>
    <text class="title" x="376" y="107" style="font-size:23px"><tspan fill="var(--blue)">Utilize –</tspan> the</text>
    <text class="title" x="376" y="134" style="font-size:23px">Future of Cloud</text>
    <text class="title" x="376" y="161" style="font-size:23px">Solutions</text>
    <text class="p"><tspan x="376" y="187">Lorem ipsum dolor sit amet, consectetur adipiscing elit.</tspan><tspan x="376" dy="7.5">Duis suscipit, arcu sed sodales dignissim, nisi ipsum</tspan><tspan x="376" dy="7.5">ultrices risus, facilisis ultrices augue urna ac tortor.</tspan><tspan x="376" dy="7.5">Donec convallis sem ac nisi posuere, ut varius erat</tspan><tspan x="376" dy="7.5">tincidunt. Integer quis tempor nunc. Ut elementum nec</tspan><tspan x="376" dy="7.5">massa sed hendrerit. Vivamus lorem risus, tempor ut</tspan><tspan x="376" dy="7.5">molestie a, rhoncus vitae massa onec sed viverra.</tspan></text>
  </g>

  <!-- Row 3 left: five columns -->
  <g transform="translate(22 712) scale(0.931)" clip-path="url(#slide-clip)">
    <rect class="slide-bg" width="610" height="342"/>
    <rect x="0" width="118" height="342" fill="var(--orange)"/>
    <rect x="118" width="124" height="342" fill="var(--blue)"/>
    <rect x="242" width="122" height="342" fill="var(--ink)"/>
    <rect x="364" width="122" height="342" fill="var(--orange)"/>
    <rect x="486" width="124" height="342" fill="var(--blue)"/>
    <g id="col1" transform="translate(59 0)">
      <circle cy="87" r="37" fill="rgba(255,255,255,.35)"/><circle cy="87" r="30" fill="var(--white)"/><circle cy="87" r="22" fill="var(--orange)"/>
      <rect x="-5" y="81" width="10" height="12" fill="none" stroke="var(--white)" stroke-width="1.2"/>
      <text class="hc" y="160">Heading 01</text>
      <text class="pc"><tspan x="0" y="170">Sub Heading will be</tspan><tspan x="0" dy="7">here</tspan></text>
      <path d="M-12 193 H12" stroke="var(--white)" stroke-width="1"/>
      <text class="pc"><tspan x="0" y="210">Lorem ipsum dolor sit</tspan><tspan x="0" dy="7">amet, consectetur</tspan><tspan x="0" dy="7">adipiscing elit, sed do</tspan><tspan x="0" dy="7">eiusmod tempor</tspan><tspan x="0" dy="7">incididunt ut labore et</tspan><tspan x="0" dy="7">dolore magna aliqua. Ut</tspan><tspan x="0" dy="7">enim ad minim veniam,</tspan><tspan x="0" dy="7">quis nostrud exercitation.</tspan></text>
    </g>
    <g transform="translate(180 0)">
      <circle cy="87" r="37" fill="rgba(255,255,255,.35)"/><circle cy="87" r="30" fill="var(--white)"/><circle cy="87" r="22" fill="#A9CBE3"/>
      <rect x="-6" y="83" width="12" height="9" fill="none" stroke="var(--white)" stroke-width="1.2"/>
      <text class="hc" y="160">Heading 02</text>
      <text class="pc"><tspan x="0" y="170">Sub Heading will be</tspan><tspan x="0" dy="7">here</tspan></text>
      <path d="M-12 193 H12" stroke="var(--white)"/>
      <text class="pc"><tspan x="0" y="210">Lorem ipsum dolor sit</tspan><tspan x="0" dy="7">amet, consectetur</tspan><tspan x="0" dy="7">adipiscing elit, sed do</tspan><tspan x="0" dy="7">eiusmod tempor</tspan><tspan x="0" dy="7">incididunt ut labore et</tspan><tspan x="0" dy="7">dolore magna aliqua. Ut</tspan><tspan x="0" dy="7">enim ad minim veniam,</tspan><tspan x="0" dy="7">quis nostrud exercitation.</tspan></text>
    </g>
    <g transform="translate(303 0)">
      <circle cy="87" r="37" fill="rgba(255,255,255,.35)"/><circle cy="87" r="30" fill="var(--white)"/><circle cy="87" r="22" fill="#888"/>
      <rect x="-6" y="81" width="12" height="12" fill="none" stroke="var(--white)" stroke-width="1.2"/>
      <text class="hc" y="162">Heading 03</text>
      <text class="pc"><tspan x="0" y="170">Sub Heading will be</tspan><tspan x="0" dy="7">here</tspan></text>
      <path d="M-12 193 H12" stroke="var(--white)"/>
      <text class="pc"><tspan x="0" y="210">Lorem ipsum dolor sit</tspan><tspan x="0" dy="7">amet, consectetur</tspan><tspan x="0" dy="7">adipiscing elit, sed do</tspan><tspan x="0" dy="7">eiusmod tempor</tspan><tspan x="0" dy="7">incididunt ut labore et</tspan><tspan x="0" dy="7">dolore magna aliqua. Ut</tspan><tspan x="0" dy="7">enim ad minim veniam,</tspan><tspan x="0" dy="7">quis nostrud exercitation.</tspan></text>
    </g>
    <g transform="translate(425 0)">
      <circle cy="87" r="37" fill="rgba(255,255,255,.35)"/><circle cy="87" r="30" fill="var(--white)"/><circle cy="87" r="22" fill="var(--orange)"/>
      <rect x="-6" y="82" width="12" height="10" fill="none" stroke="var(--white)" stroke-width="1.2"/>
      <text class="hc" y="160">Heading 04</text>
      <text class="pc"><tspan x="0" y="170">Sub Heading will be</tspan><tspan x="0" dy="7">here</tspan></text>
      <path d="M-12 193 H12" stroke="var(--white)"/>
      <text class="pc"><tspan x="0" y="210">Lorem ipsum dolor sit</tspan><tspan x="0" dy="7">amet, consectetur</tspan><tspan x="0" dy="7">adipiscing elit, sed do</tspan><tspan x="0" dy="7">eiusmod tempor</tspan><tspan x="0" dy="7">incididunt ut labore et</tspan><tspan x="0" dy="7">dolore magna aliqua. Ut</tspan><tspan x="0" dy="7">enim ad minim veniam,</tspan><tspan x="0" dy="7">quis nostrud exercitation.</tspan></text>
    </g>
    <g transform="translate(548 0)">
      <circle cy="87" r="37" fill="rgba(255,255,255,.35)"/><circle cy="87" r="30" fill="var(--white)"/><circle cy="87" r="22" fill="var(--white)"/>
      <rect x="-6" y="81" width="12" height="12" fill="none" stroke="var(--ink)" stroke-width="1.2"/>
      <text class="hc" y="160">Heading 05</text>
      <text class="pc"><tspan x="0" y="170">Sub Heading will be</tspan><tspan x="0" dy="7">here</tspan></text>
      <path d="M-12 193 H12" stroke="var(--white)"/>
      <text class="pc"><tspan x="0" y="210">Lorem ipsum dolor sit</tspan><tspan x="0" dy="7">amet, consectetur</tspan><tspan x="0" dy="7">adipiscing elit, sed do</tspan><tspan x="0" dy="7">eiusmod tempor</tspan><tspan x="0" dy="7">incididunt ut labore et</tspan><tspan x="0" dy="7">dolore magna aliqua. Ut</tspan><tspan x="0" dy="7">enim ad minim veniam,</tspan><tspan x="0" dy="7">quis nostrud exercitation.</tspan></text>
    </g>
  </g>

  <!-- Row 3 right: cloud percentages -->
  <g transform="translate(610 712) scale(0.931)" clip-path="url(#slide-clip)">
    <rect class="slide-bg" width="610" height="342"/>
    <use href="#logo" x="520" y="56"/>
    <text class="title" x="305" y="56" style="font-size:21px;text-anchor:middle">INFOGRAPHIC MOCKUP</text>
    <text class="pc"><tspan x="305" y="77">Lorem ipsum dolor sit amet, consectetur adipiscing elit. Duis suscipit, arcu sed sodales dignissim, nisi ipsum ultrices</tspan><tspan x="305" dy="7">risus, facilisis ultrices augue urna ac tortor. Donec convallis sem ac nisi posuere, ut varius erat tincidunt integer quis.</tspan></text>
    <use href="#cloud" x="58" y="108" width="108" height="66" fill="var(--orange)"/>
    <text class="pct" x="112" y="151">85%</text>
    <use href="#down-arrow" x="107" y="160" width="10" height="22" fill="var(--white)"/>
    <text class="hc" x="112" y="214">Data A</text>
    <text class="pc"><tspan x="112" y="223">Lorem ipsum dolor sit amet,</tspan><tspan x="112" dy="7">consectetur adipiscing elit. Duis</tspan><tspan x="112" dy="7">suscipit, arcu sed sodales.</tspan></text>
    <use href="#cloud" x="185" y="165" width="108" height="66" fill="var(--blue)"/>
    <text class="pct" x="239" y="208">80%</text>
    <use href="#down-arrow" x="234" y="217" width="10" height="22" fill="var(--white)"/>
    <text class="hc" x="239" y="271">Data B</text>
    <text class="pc"><tspan x="239" y="280">Lorem ipsum dolor sit amet,</tspan><tspan x="239" dy="7">consectetur adipiscing elit. Duis</tspan><tspan x="239" dy="7">suscipit, arcu sed sodales.</tspan></text>
    <use href="#cloud" x="313" y="108" width="108" height="66" fill="var(--white)"/>
    <text class="pct" x="367" y="151" style="fill:var(--black)">83%</text>
    <use href="#down-arrow" x="362" y="160" width="10" height="22" fill="#444"/>
    <text class="hc" x="367" y="214">Data C</text>
    <text class="pc"><tspan x="367" y="223">Lorem ipsum dolor sit amet,</tspan><tspan x="367" dy="7">consectetur adipiscing elit. Duis</tspan><tspan x="367" dy="7">suscipit, arcu sed sodales.</tspan></text>
    <use href="#cloud" x="441" y="165" width="108" height="66" fill="var(--orange)"/>
    <text class="pct" x="495" y="208">88%</text>
    <use href="#down-arrow" x="490" y="217" width="10" height="22" fill="var(--white)"/>
    <text class="hc" x="495" y="271">Data D</text>
    <text class="pc"><tspan x="495" y="280">Lorem ipsum dolor sit amet,</tspan><tspan x="495" dy="7">consectetur adipiscing elit. Duis</tspan><tspan x="495" dy="7">suscipit, arcu sed sodales.</tspan></text>
    <g stroke="var(--light)" stroke-width="1.2" fill="none">
      <path d="M172 168 L190 184 M172 168 l0 5 M172 168 l5 0 M190 184 l-5 0 M190 184 l0 -5"/>
      <path d="M288 184 L306 168 M306 168 l-5 0 M306 168 l0 5 M288 184 l5 0 M288 184 l0 -5"/>
      <path d="M428 168 L446 184 M428 168 l0 5 M428 168 l5 0 M446 184 l-5 0 M446 184 l0 -5"/>
    </g>
  </g>

  <!-- Row 4 left: bar chart -->
  <g transform="translate(22 1040) scale(0.931)" clip-path="url(#slide-clip)">
    <rect class="slide-bg" width="610" height="342"/>
    <use href="#logo" x="520" y="56"/>
    <text class="title" x="305" y="56" style="font-size:21px;text-anchor:middle">INFOGRAPHIC MOCKUP</text>
    <text class="pc"><tspan x="305" y="77">Lorem ipsum dolor sit amet, consectetur adipiscing elit. Duis suscipit, arcu sed sodales dignissim, nisi ipsum ultrices</tspan><tspan x="305" dy="7">risus, facilisis ultrices augue urna ac tortor. Donec convallis sem ac nisi posuere, ut varius erat tincidunt integer quis.</tspan></text>
    <g>
      <rect x="228" y="114" width="29" height="170" rx="14.5" fill="var(--white)"/>
      <rect x="228" y="140" width="29" height="144" rx="14.5" fill="var(--orange)"/>
      <rect x="269" y="114" width="29" height="170" rx="14.5" fill="var(--white)"/>
      <rect x="269" y="165" width="29" height="119" rx="14.5" fill="var(--blue)"/>
      <rect x="310" y="114" width="29" height="170" rx="14.5" fill="var(--white)"/>
      <rect x="310" y="148" width="29" height="136" rx="14.5" fill="var(--orange)"/>
      <rect x="351" y="114" width="29" height="170" rx="14.5" fill="var(--white)"/>
      <rect x="351" y="155" width="29" height="129" rx="14.5" fill="var(--blue)"/>
      <text style="font-size:7px;font-weight:700;fill:var(--white);text-anchor:middle"><tspan x="242" y="274">85%</tspan><tspan x="283" y="274">75%</tspan><tspan x="324" y="274">80%</tspan><tspan x="365" y="274">78%</tspan></text>
      <text class="hc"><tspan x="242" y="304">A</tspan><tspan x="283" y="304">B</tspan><tspan x="324" y="304">C</tspan><tspan x="365" y="304">D</tspan></text>
    </g>
    <path class="line-o" d="M150 130 H166"/><circle cx="150" cy="130" r="2.5" fill="var(--orange)"/>
    <circle cx="195" cy="148" r="9" fill="none" stroke="var(--orange)"/>
    <text class="h" x="168" y="151" style="text-anchor:end">Category A</text>
    <text class="p" style="text-anchor:end"><tspan x="168" y="161">Lorem ipsum dolor sit amet,</tspan><tspan x="168" dy="7">consectetur adipiscing elit. Duis</tspan><tspan x="168" dy="7">suscipit, arcu sed sodales dignissim,</tspan><tspan x="168" dy="7">nisi ipsum ultrices risus, facilisis ultrices</tspan><tspan x="168" dy="7">augue urna.</tspan></text>
    <path class="line-o" d="M150 245 H166"/><circle cx="150" cy="245" r="2.5" fill="var(--orange)"/>
    <rect x="186" y="229" width="18" height="16" fill="none" stroke="var(--orange)"/>
    <text class="h" x="168" y="248" style="text-anchor:end">Category B</text>
    <text class="p" style="text-anchor:end;fill:#333"><tspan x="168" y="258">Lorem ipsum dolor sit amet,</tspan><tspan x="168" dy="7">consectetur adipiscing elit. Duis</tspan><tspan x="168" dy="7">suscipit, arcu sed sodales dignissim,</tspan><tspan x="168" dy="7">nisi ipsum ultrices risus, facilisis ultrices</tspan><tspan x="168" dy="7">augue urna.</tspan></text>
    <path d="M460 130 H444" stroke="var(--blue)"/><circle cx="460" cy="130" r="2.5" fill="var(--blue)"/>
    <circle cx="413" cy="148" r="9" fill="none" stroke="var(--blue)"/>
    <text class="h" x="440" y="151">Category C</text>
    <text class="p"><tspan x="440" y="161">Lorem ipsum dolor sit amet,</tspan><tspan x="440" dy="7">consectetur adipiscing elit. Duis</tspan><tspan x="440" dy="7">suscipit, arcu sed sodales dignissim,</tspan><tspan x="440" dy="7">nisi ipsum ultrices risus, facilisis ultrices</tspan><tspan x="440" dy="7">augue urna.</tspan></text>
    <path d="M460 190 H444" stroke="var(--blue)"/><circle cx="460" cy="190" r="2.5" fill="var(--blue)"/>
    <rect x="404" y="230" width="18" height="16" fill="none" stroke="var(--blue)"/>
    <text class="h" x="440" y="248">Category D</text>
    <text class="p"><tspan x="440" y="258">Lorem ipsum dolor sit amet,</tspan><tspan x="440" dy="7">consectetur adipiscing elit. Duis</tspan><tspan x="440" dy="7">suscipit, arcu sed sodales dignissim,</tspan><tspan x="440" dy="7">nisi ipsum ultrices risus, facilisis ultrices</tspan><tspan x="440" dy="7">augue urna.</tspan></text>
  </g>

  <!-- Row 4 right: hub -->
  <g transform="translate(610 1040) scale(0.931)" clip-path="url(#slide-clip)">
    <rect class="slide-bg" width="610" height="342"/>
    <use href="#logo" x="520" y="56"/>
    <text class="title" x="305" y="56" style="font-size:21px;text-anchor:middle">INFOGRAPHIC MOCKUP</text>
    <text class="pc"><tspan x="305" y="77">Lorem ipsum dolor sit amet, consectetur adipiscing elit. Duis suscipit, arcu sed sodales dignissim, nisi ipsum ultrices</tspan><tspan x="305" dy="7">risus, facilisis ultrices augue urna ac tortor. Donec convallis sem ac nisi posuere, ut varius erat tincidunt integer quis.</tspan></text>
    <path d="M283 170 L305 160 L327 170 L327 196 L305 206 L283 196 Z" fill="var(--white)"/>
    <path d="M283 170 L305 180 L327 170 M305 180 V206" stroke="var(--black)" stroke-width="2" fill="none"/>
    <text class="hc" x="305" y="225">Title Here</text>
    <text class="pc"><tspan x="305" y="234">Lorem ipsum dolor sit amet,</tspan><tspan x="305" dy="7">consectetur adipiscing elit. Duis</tspan><tspan x="305" dy="7">suscipit, arcu sed sodales dignissim,</tspan><tspan x="305" dy="7">nisi ipsum ultrices risus facilisis.</tspan></text>
    <g class="line-o"><path d="M218 147 H240 V183 H262 M218 245 H240 V183"/></g>
    <circle cx="218" cy="147" r="2.5" fill="var(--orange)"/><circle cx="218" cy="245" r="2.5" fill="var(--orange)"/><circle cx="262" cy="183" r="2.5" fill="var(--orange)"/>
    <g stroke="var(--blue)" fill="none"><path d="M392 147 H370 V183 H348 M392 245 H370 V183"/></g>
    <circle cx="392" cy="147" r="2.5" fill="var(--blue)"/><circle cx="392" cy="245" r="2.5" fill="var(--blue)"/><circle cx="348" cy="183" r="2.5" fill="var(--blue)"/>
    <use href="#cloud" x="134" y="126" width="76" height="46" fill="var(--orange)"/>
    <text class="pct" x="172" y="158" style="font-size:11px">88%</text>
    <use href="#down-arrow" x="160" y="164" width="7" height="15" fill="var(--white)"/><use href="#down-arrow" x="174" y="164" width="7" height="15" fill="var(--white)"/>
    <use href="#cloud" x="134" y="224" width="76" height="46" fill="var(--orange)"/>
    <text class="pct" x="172" y="256" style="font-size:11px">83%</text>
    <use href="#down-arrow" x="160" y="262" width="7" height="15" fill="var(--white)"/><use href="#down-arrow" x="174" y="262" width="7" height="15" fill="var(--white)"/>
    <use href="#cloud" x="400" y="126" width="76" height="46" fill="var(--blue)"/>
    <text class="pct" x="438" y="158" style="font-size:11px">91%</text>
    <use href="#down-arrow" x="426" y="164" width="7" height="15" fill="var(--white)"/><use href="#down-arrow" x="440" y="164" width="7" height="15" fill="var(--white)"/>
    <use href="#cloud" x="400" y="224" width="76" height="46" fill="var(--blue)"/>
    <text class="pct" x="438" y="256" style="font-size:11px">86%</text>
    <use href="#down-arrow" x="426" y="262" width="7" height="15" fill="var(--white)"/><use href="#down-arrow" x="440" y="262" width="7" height="15" fill="var(--white)"/>
    <text class="h" x="124" y="133" style="text-anchor:end">Data A</text>
    <text class="p" style="text-anchor:end"><tspan x="124" y="143">Lorem ipsum dolor sit</tspan><tspan x="124" dy="7">amet, consectetur</tspan><tspan x="124" dy="7">adipiscing elit. Duis</tspan><tspan x="124" dy="7">suscipit, arcu sed sodales</tspan><tspan x="124" dy="7">dignissim nisi.</tspan></text>
    <text class="h" x="124" y="231" style="text-anchor:end">Data B</text>
    <text class="p" style="text-anchor:end"><tspan x="124" y="241">Lorem ipsum dolor sit</tspan><tspan x="124" dy="7">amet, consectetur</tspan><tspan x="124" dy="7">adipiscing elit. Duis</tspan><tspan x="124" dy="7">suscipit, arcu sed sodales</tspan><tspan x="124" dy="7">dignissim nisi.</tspan></text>
    <text class="h" x="486" y="133">Data C</text>
    <text class="p"><tspan x="486" y="143">Lorem ipsum dolor sit</tspan><tspan x="486" dy="7">amet, consectetur</tspan><tspan x="486" dy="7">adipiscing elit. Duis</tspan><tspan x="486" dy="7">suscipit, arcu sed sodales</tspan><tspan x="486" dy="7">dignissim nisi.</tspan></text>
    <text class="h" x="486" y="231">Data D</text>
    <text class="p"><tspan x="486" y="241">Lorem ipsum dolor sit</tspan><tspan x="486" dy="7">amet, consectetur</tspan><tspan x="486" dy="7">adipiscing elit. Duis</tspan><tspan x="486" dy="7">suscipit, arcu sed sodales</tspan><tspan x="486" dy="7">dignissim nisi.</tspan></text>
  </g>

  <!-- Row 5 left: arc categories -->
  <g transform="translate(22 1368) scale(0.931)" clip-path="url(#slide-clip)">
    <rect class="slide-bg" width="610" height="342"/>
    <use href="#logo" x="520" y="56"/>
    <text class="title" x="305" y="56" style="font-size:21px;text-anchor:middle">INFOGRAPHIC MOCKUP</text>
    <text class="pc"><tspan x="305" y="77">Lorem ipsum dolor sit amet, consectetur adipiscing elit. Duis suscipit, arcu sed sodales dignissim, nisi ipsum ultrices</tspan><tspan x="305" dy="7">risus, facilisis ultrices augue urna ac tortor. Donec convallis sem ac nisi posuere, ut varius erat tincidunt integer quis.</tspan></text>
    <path class="line-o" d="M208 282 A98 98 0 0 1 402 282"/>
    <circle cx="208" cy="282" r="2.5" fill="var(--orange)"/><circle cx="402" cy="282" r="2.5" fill="var(--orange)"/>
    <g stroke="#777" fill="none"><path d="M220 128 H280 V180 M330 180 V128 H390 M128 226 H220 M390 226 H482"/></g>
    <circle cx="220" cy="128" r="2.5" fill="var(--orange)"/><circle cx="390" cy="128" r="2.5" fill="var(--orange)"/><circle cx="220" cy="226" r="2.5" fill="var(--orange)"/><circle cx="482" cy="226" r="2.5" fill="var(--orange)"/>
    <use href="#cloud" x="244" y="215" width="122" height="74" fill="var(--orange)"/>
    <text class="hc" x="305" y="262">Title Here</text>
    <use href="#down-arrow" x="296" y="274" width="18" height="36" fill="var(--white)"/>
    <circle cx="192" cy="127" r="20" fill="var(--orange)"/><circle cx="412" cy="127" r="20" fill="var(--orange)"/>
    <circle cx="103" cy="226" r="20" fill="var(--orange)"/><circle cx="507" cy="226" r="20" fill="var(--orange)"/>
    <g stroke="var(--white)" fill="none" stroke-width="1"><rect x="185" y="120" width="14" height="14"/><rect x="405" y="120" width="14" height="14"/><circle cx="103" cy="226" r="7"/><circle cx="507" cy="226" r="7"/></g>
    <text class="hc" x="192" y="164">Category Two</text>
    <text class="pc"><tspan x="192" y="174">Lorem ipsum dolor sit amet,</tspan><tspan x="192" dy="7">consectetur adipiscing elit duis suscipit</tspan><tspan x="192" dy="7">arcu sed.</tspan></text>
    <text class="hc" x="412" y="164">Category Three</text>
    <text class="pc"><tspan x="412" y="174">Lorem ipsum dolor sit amet,</tspan><tspan x="412" dy="7">consectetur adipiscing elit duis suscipit</tspan><tspan x="412" dy="7">arcu sed.</tspan></text>
    <text class="hc" x="103" y="262">Category One</text>
    <text class="pc"><tspan x="103" y="272">Lorem ipsum dolor sit amet,</tspan><tspan x="103" dy="7">consectetur adipiscing elit duis suscipit</tspan><tspan x="103" dy="7">arcu sed.</tspan></text>
    <text class="hc" x="507" y="262">Category Four</text>
    <text class="pc"><tspan x="507" y="272">Lorem ipsum dolor sit amet,</tspan><tspan x="507" dy="7">consectetur adipiscing elit duis suscipit</tspan><tspan x="507" dy="7">arcu sed.</tspan></text>
  </g>

  <!-- Row 5 right: globe -->
  <g transform="translate(610 1368) scale(0.931)" clip-path="url(#slide-clip)">
    <rect class="slide-bg" width="610" height="342"/>
    <use href="#logo" x="520" y="56"/>
    <text class="title" x="305" y="56" style="font-size:21px;text-anchor:middle">INFOGRAPHIC MOCKUP</text>
    <text class="pc"><tspan x="305" y="77">Lorem ipsum dolor sit amet, consectetur adipiscing elit. Duis suscipit, arcu sed sodales dignissim, nisi ipsum ultrices</tspan><tspan x="305" dy="7">risus, facilisis ultrices augue urna ac tortor. Donec convallis sem ac nisi posuere, ut varius erat tincidunt integer quis.</tspan></text>
    <text class="hc" x="305" y="118">Title Here</text>
    <use href="#cloud" x="158" y="150" width="84" height="44" fill="var(--orange)"/>
    <use href="#down-arrow" x="196" y="183" width="9" height="20" fill="var(--white)"/>
    <use href="#cloud" x="350" y="150" width="84" height="44" fill="var(--blue)"/>
    <use href="#down-arrow" x="394" y="183" width="9" height="20" fill="var(--white)"/>
    <use href="#cloud" x="238" y="150" width="134" height="62" fill="var(--white)"/>
    <circle cx="305" cy="160" r="34" fill="var(--orange)" role="img" aria-label="World map globe in orange and black"/>
    <path d="M305 212 V222" stroke="#777"/><circle cx="305" cy="225" r="3" fill="none" stroke="#777"/>
    <path d="M97 238 H513 M97 238 V252 M236 238 V252 M374 238 V252 M513 238 V252" stroke="#777" fill="none"/>
    <g fill="var(--white)"><circle cx="97" cy="252" r="2.5"/><circle cx="236" cy="252" r="2.5"/><circle cx="374" cy="252" r="2.5"/><circle cx="513" cy="252" r="2.5"/></g>
    <text class="hc" x="97" y="270">Category One</text>
    <text class="pc"><tspan x="97" y="280">Lorem ipsum dolor sit amet,</tspan><tspan x="97" dy="7">consectetur adipiscing elit. Duis</tspan><tspan x="97" dy="7">suscipit, arcu sed sodales dignissi.</tspan></text>
    <text class="hc" x="236" y="270">Category Two</text>
    <text class="pc"><tspan x="236" y="280">Lorem ipsum dolor sit amet,</tspan><tspan x="236" dy="7">consectetur adipiscing elit. Duis</tspan><tspan x="236" dy="7">suscipit, arcu sed sodales dignissi.</tspan></text>
    <text class="hc" x="374" y="270">Category Three</text>
    <text class="pc"><tspan x="374" y="280">Lorem ipsum dolor sit amet,</tspan><tspan x="374" dy="7">consectetur adipiscing elit. Duis</tspan><tspan x="374" dy="7">suscipit, arcu sed sodales dignissi.</tspan></text>
    <text class="hc" x="513" y="270">Category Four</text>
    <text class="pc"><tspan x="513" y="280">Lorem ipsum dolor sit amet,</tspan><tspan x="513" dy="7">consectetur adipiscing elit. Duis</tspan><tspan x="513" dy="7">suscipit, arcu sed sodales dignissi.</tspan></text>
  </g>

  <!-- Row 6 left: cloud timeline -->
  <g transform="translate(22 1696) scale(0.931)" clip-path="url(#slide-clip)">
    <rect class="slide-bg" width="610" height="342"/>
    <use href="#logo" x="520" y="56"/>
    <text class="title" x="305" y="56" style="font-size:21px;text-anchor:middle">INFOGRAPHIC MOCKUP</text>
    <text class="pc"><tspan x="305" y="77">Lorem ipsum dolor sit amet, consectetur adipiscing elit. Duis suscipit, arcu sed sodales dignissim, nisi ipsum ultrices</tspan><tspan x="305" dy="7">risus, facilisis ultrices augue urna ac tortor. Donec convallis sem ac nisi posuere, ut varius erat tincidunt integer quis.</tspan></text>
    <path d="M88 206 H524" stroke="#777"/>
    <path d="M88 222 V236 M305 222 V236 M522 222 V236 M196 190 V168 M413 190 V168" stroke="#777"/>
    <g fill="var(--white)"><circle cx="88" cy="236" r="2.5"/><circle cx="305" cy="236" r="2.5"/><circle cx="522" cy="236" r="2.5"/><circle cx="196" cy="168" r="2.5"/><circle cx="413" cy="168" r="2.5"/></g>
    <use href="#cloud" x="50" y="182" width="76" height="44" fill="var(--white)"/><circle cx="88" cy="208" r="13" fill="var(--orange)"/>
    <use href="#cloud" x="158" y="182" width="76" height="44" fill="var(--blue)"/><circle cx="196" cy="208" r="13" fill="var(--blue)" stroke="var(--white)"/>
    <use href="#cloud" x="267" y="182" width="76" height="44" fill="var(--white)"/><circle cx="305" cy="208" r="13" fill="var(--white)" stroke="#999"/>
    <use href="#cloud" x="375" y="182" width="76" height="44" fill="var(--blue)"/><circle cx="413" cy="208" r="13" fill="var(--blue)" stroke="var(--white)"/>
    <use href="#cloud" x="484" y="182" width="76" height="44" fill="var(--orange)"/><circle cx="522" cy="208" r="13" fill="var(--orange)" stroke="var(--white)"/>
    <text class="hc" x="196" y="128">Category Two</text>
    <text class="pc"><tspan x="196" y="138">Lorem ipsum dolor sit amet,</tspan><tspan x="196" dy="7">consectetur adipiscing elit.</tspan><tspan x="196" dy="7">Duis suscipit, arcu sed</tspan><tspan x="196" dy="7">sodales dig.</tspan></text>
    <text class="hc" x="413" y="128">Category Four</text>
    <text class="pc"><tspan x="413" y="138">Lorem ipsum dolor sit amet,</tspan><tspan x="413" dy="7">consectetur adipiscing elit.</tspan><tspan x="413" dy="7">Duis suscipit, arcu sed</tspan><tspan x="413" dy="7">sodales dig.</tspan></text>
    <text class="hc" x="88" y="270">Category One</text>
    <text class="pc"><tspan x="88" y="280">Lorem ipsum dolor sit amet,</tspan><tspan x="88" dy="7">consectetur adipiscing elit.</tspan><tspan x="88" dy="7">Duis suscipit, arcu sed</tspan><tspan x="88" dy="7">sodales dig.</tspan></text>
    <text class="hc" x="305" y="270">Category Three</text>
    <text class="pc"><tspan x="305" y="280">Lorem ipsum dolor sit amet,</tspan><tspan x="305" dy="7">consectetur adipiscing elit.</tspan><tspan x="305" dy="7">Duis suscipit, arcu sed</tspan><tspan x="305" dy="7">sodales dig.</tspan></text>
    <text class="hc" x="522" y="270">Category Five</text>
    <text class="pc"><tspan x="522" y="280">Lorem ipsum dolor sit amet,</tspan><tspan x="522" dy="7">consectetur adipiscing elit.</tspan><tspan x="522" dy="7">Duis suscipit, arcu sed</tspan><tspan x="522" dy="7">sodales dig.</tspan></text>
  </g>

  <!-- Row 6 right: stepped arrows -->
  <g transform="translate(610 1696) scale(0.931)" clip-path="url(#slide-clip)">
    <rect class="slide-bg" width="610" height="342"/>
    <use href="#logo" x="520" y="56"/>
    <text class="title" x="305" y="56" style="font-size:21px;text-anchor:middle">ARROW INFOGRAPHIC SLIDE</text>
    <polygon points="166,150 300,150 300,133 324,162 300,192 300,175 166,175" fill="var(--blue)"/>
    <polygon points="0,190 150,190 150,168 202,204 150,240 150,218 0,218" fill="var(--orange)"/>
    <polygon points="346,180 420,180 420,160 474,196 420,232 420,212 346,212" fill="var(--blue)"/>
    <polygon points="272,196 344,196 344,178 398,214 344,250 344,232 272,232" fill="var(--orange)"/>
    <polygon points="432,196 500,196 500,176 552,214 500,252 500,232 432,232" fill="var(--orange)"/>
    <text class="num" x="86" y="209">01</text><text class="num" x="230" y="167">02</text><text class="num" x="314" y="219">03</text><text class="num" x="398" y="198">04</text><text class="num" x="478" y="219">05</text>
    <g fill="none" stroke="var(--white)"><circle cx="170" cy="203" r="6"/><circle cx="290" cy="162" r="6"/><rect x="356" y="206" width="10" height="14"/><circle cx="441" cy="197" r="6"/><circle cx="518" cy="214" r="6"/></g>
    <g>
      <text class="hc" x="228" y="99" style="font-size:9px">Insert Title Here</text>
      <text class="pc" style="font-size:7px"><tspan x="228" y="112">It's now that much</tspan><tspan x="228" dy="12">easier and more</tspan><tspan x="228" dy="12">effective to start, Lorem</tspan></text>
      <text class="hc" x="381" y="99" style="font-size:9px">Insert Title Here</text>
      <text class="pc" style="font-size:7px"><tspan x="381" y="112">It's now that much</tspan><tspan x="381" dy="12">easier and more</tspan><tspan x="381" dy="12">effective to start, Lorem</tspan></text>
      <text class="hc" x="88" y="256" style="font-size:9px">Insert Title Here</text>
      <text class="pc" style="font-size:7px"><tspan x="88" y="269">It's now that much</tspan><tspan x="88" dy="12">easier and more</tspan><tspan x="88" dy="12">effective to start, Lorem</tspan></text>
      <text class="hc" x="302" y="273" style="font-size:9px">Insert Title Here</text>
      <text class="pc" style="font-size:7px"><tspan x="302" y="286">It's now that much</tspan><tspan x="302" dy="12">easier and more</tspan><tspan x="302" dy="12">effective to start, Lorem</tspan></text>
      <text class="hc" x="458" y="273" style="font-size:9px">Insert Title Here</text>
      <text class="pc" style="font-size:7px"><tspan x="458" y="286">It's now that much</tspan><tspan x="458" dy="12">easier and more</tspan><tspan x="458" dy="12">effective to start, Lorem</tspan></text>
    </g>
  </g>

  <!-- Row 7 left: ribbon arrows -->
  <g transform="translate(22 2024) scale(0.931)" clip-path="url(#slide-clip)">
    <rect class="slide-bg" width="610" height="342"/>
    <use href="#logo" x="520" y="56"/>
    <text class="title" x="305" y="56" style="font-size:21px;text-anchor:middle">ARROW INFOGRAPHIC SLIDE</text>
    <polygon points="43,188 108,188 108,302 76,282 43,302" fill="var(--orange)"/>
    <polygon points="108,188 136,188 136,258 108,258" fill="var(--light)"/>
    <rect x="136" y="188" width="65" height="58" fill="var(--orange)"/>
    <polygon points="201,188 229,188 229,258 201,246" fill="var(--light)"/>
    <rect x="229" y="188" width="65" height="58" fill="var(--blue)"/>
    <polygon points="294,188 320,188 320,258 294,246" fill="var(--light)"/>
    <rect x="320" y="188" width="65" height="58" fill="var(--blue)"/>
    <polygon points="385,188 412,188 412,258 385,246" fill="var(--light)"/>
    <rect x="412" y="188" width="65" height="58" fill="var(--grey)"/>
    <polygon points="477,188 503,188 503,258 477,246" fill="var(--light)"/>
    <polygon points="503,140 535,114 567,140 567,246 503,246" fill="var(--grey)"/>
    <g fill="none" stroke="var(--white)"><rect x="66" y="208" width="18" height="14"/><circle cx="168" cy="216" r="7"/><rect x="252" y="208" width="18" height="14"/><rect x="344" y="208" width="16" height="16"/><rect x="435" y="209" width="20" height="12"/><circle cx="535" cy="216" r="8"/></g>
    <g>
      <text class="hc" x="76" y="108" style="font-size:9px">Insert Title Here</text>
      <text class="pc" style="font-size:7px"><tspan x="76" y="121">It's now that much</tspan><tspan x="76" dy="12">easier and more</tspan><tspan x="76" dy="12">effective to start, Lorem</tspan></text>
      <text class="hc" x="261" y="108" style="font-size:9px">Insert Title Here</text>
      <text class="pc" style="font-size:7px"><tspan x="261" y="121">It's now that much</tspan><tspan x="261" dy="12">easier and more</tspan><tspan x="261" dy="12">effective to start, Lorem</tspan></text>
      <text class="hc" x="445" y="108" style="font-size:9px">Insert Title Here</text>
      <text class="pc" style="font-size:7px"><tspan x="445" y="121">It's now that much</tspan><tspan x="445" dy="12">easier and more</tspan><tspan x="445" dy="12">effective to start, Lorem</tspan></text>
      <text class="hc" x="168" y="269" style="font-size:9px">Insert Title Here</text>
      <text class="pc" style="font-size:7px"><tspan x="168" y="282">It's now that much</tspan><tspan x="168" dy="12">easier and more</tspan><tspan x="168" dy="12">effective to start, Lorem</tspan></text>
      <text class="hc" x="352" y="269" style="font-size:9px">Insert Title Here</text>
      <text class="pc" style="font-size:7px"><tspan x="352" y="282">It's now that much</tspan><tspan x="352" dy="12">easier and more</tspan><tspan x="352" dy="12">effective to start, Lorem</tspan></text>
      <text class="hc" x="535" y="269" style="font-size:9px">Insert Title Here</text>
      <text class="pc" style="font-size:7px"><tspan x="535" y="282">It's now that much</tspan><tspan x="535" dy="12">easier and more</tspan><tspan x="535" dy="12">effective to start, Lorem</tspan></text>
    </g>
  </g>

  <!-- Row 7 right: circle zigzag -->
  <g transform="translate(610 2024) scale(0.931)" clip-path="url(#slide-clip)">
    <rect class="slide-bg" width="610" height="342"/>
    <use href="#logo" x="520" y="56"/>
    <text class="title" x="305" y="56" style="font-size:17px;text-anchor:middle">CIRCLE INFOGRAPHIC SLIDE</text>
    <text class="pc" x="305" y="72">Letterpress next level trust fund, before they sold out +1 meh gluten-free locavore tacos PBR&amp;B tofu.</text>
    <g stroke="var(--white)" stroke-width="5" fill="none">
      <path d="M0 108 L88 152 L194 206 L305 264 L416 206 L522 152 L610 108"/>
      <path d="M0 124 L88 168 L194 222 L305 280 L416 222 L522 168 L610 124" stroke="var(--light)"/>
      <path d="M0 140 L88 184 L194 238 L305 296 L416 238 L522 184 L610 140" stroke="var(--grey)"/>
    </g>
    <g>
      <polygon points="38,158 88,136 138,158 88,184" fill="var(--blue)"/>
      <polygon points="144,220 194,198 244,220 194,246" fill="var(--orange)"/>
      <polygon points="255,276 305,254 355,276 305,302" fill="var(--blue)"/>
      <polygon points="366,220 416,198 466,220 416,246" fill="var(--orange)"/>
      <polygon points="472,158 522,136 572,158 522,184" fill="var(--blue)"/>
    </g>
    <g fill="var(--white)" stroke="var(--black)" stroke-width="1.5">
      <circle cx="88" cy="136" r="24"/><circle cx="194" cy="198" r="24"/><circle cx="305" cy="254" r="24"/><circle cx="416" cy="198" r="24"/><circle cx="522" cy="136" r="24"/>
    </g>
    <g fill="none" stroke="var(--ink)"><rect x="82" y="131" width="12" height="10"/><rect x="188" y="192" width="12" height="12"/><circle cx="305" cy="254" r="6"/><rect x="410" y="193" width="12" height="10"/><rect x="516" y="130" width="12" height="12"/></g>
    <text class="pc"><tspan x="88" y="92">Synth chartreuse XOXO,</tspan><tspan x="88" dy="9">tacos brooklyn VHS</tspan><tspan x="88" dy="9">plaid.</tspan></text>
    <text class="pc"><tspan x="194" y="148">Synth chartreuse XOXO,</tspan><tspan x="194" dy="9">tacos brooklyn VHS</tspan><tspan x="194" dy="9">plaid.</tspan></text>
    <text class="pc"><tspan x="305" y="204">Synth chartreuse XOXO,</tspan><tspan x="305" dy="9">tacos brooklyn VHS</tspan><tspan x="305" dy="9">plaid.</tspan></text>
    <text class="pc"><tspan x="416" y="148">Synth chartreuse XOXO,</tspan><tspan x="416" dy="9">tacos brooklyn VHS</tspan><tspan x="416" dy="9">plaid.</tspan></text>
    <text class="pc"><tspan x="522" y="92">Synth chartreuse XOXO,</tspan><tspan x="522" dy="9">tacos brooklyn VHS</tspan><tspan x="522" dy="9">plaid.</tspan></text>
  </g>
</svg>
</body>
</html>
```